Wordpress Design Project

We are a new global agency focused on social, digital development for major brands, we want our site to have a pinterest concept like this one- http://plumvaultmarket.net/item/ripple-long-page-blog-theme/full_screen_preview/5417093 with clean darker layout like this- http://demo.brovakits.com/?theme=lowglider
http://www.qemtaro.com/wp/drapecase/
Also see these links for the organic look and feel we are going for, we want clean, simple, fun- different. Not corporate.
Link 1- http://pixelharborjournal.com/inspiration/top-page-layouts-of-2012
Link 2- http://www.marrowstudiohub.com/2008/12/100-pages-with-remarkable-handmade-styling/

We want a clean, organic looking site that ties into the brand personality and color theme. Nothing too corporate looking. Think social, think fun, think I want to hire this agency! We want it wordpress based. Something really cool as far as image or click through illustration of some sort would be awesome.
Updates

Reason: In looking at initial designs, they are too corporate, we want more organic, clean, different, fun- see these links for examples, we are also going to guarantee project and do not just copy the file photos that we sent- that is just to show the brand logo etc...- http://pixelharborjournal.com/inspiration/top-page-layouts-of-2012 another link- http://www.marrowstudiohub.com/2008/12/100-pages-with-remarkable-handmade-styling/

In looking at initial designs, they are too corporate, we want more organic, clean, different, fun- see these links for examples, we are also just guaranteed the project. Please do not just copy the file photos that we sent- that is just to show the brand logo etc...- see these links for the type of style/design we are looking for: http://pixelharborjournal.com/inspiration/top-page-layouts-of-2012
another link- http://www.marrowstudiohub.com/2008/12/100-pages-with-remarkable-handmade-styling/

Target Market(s)

All of the below should be budget-holding decision makers of over $1mm in marketing annually:
- High level executives who want a new kind of agency.
- Marketing leaders who want to include social media to drive better results.
- Company executives who are passionate about connecting with consumers.

Industry/Entity Type

Digital

Requirements
Must have
• Clean and not too busy.
Stylish: Not too boxy or corporate looking.
Good use of textures as opposed to too many solid colors..
Friendly and personable.
Nice to have
• Original and energetic.
Make good use of making a Wordpress template not look too templated by overlapping images, making 3d and crafty enhancements to graphics.
Angular elements that reinforce the brand logo.
Boxed areas, if necessary, should be de-emphasized with good use of subtle colors.
Expanded complimentary color palette.
Consider photo or graphic elements that don't look too much like stock - maybe macro photo elements, illustrations or iconography.
Should not have
• Not too many competing elements.

```html
<!DOCTYPE html>
<html lang="en">
<head>
<meta charset="utf-8">
<title>RALLY — Social Digital Agency</title>
<link href="https://fonts.googleapis.com/css2?family=Open+Sans:wght@400;600&family=Raleway:wght@200;300;800&family=Roboto+Condensed:wght@400;700&display=swap" rel="stylesheet">
<style>
:root{
  --green:#8cc43f;
  --ink:#1d1d1f;
  --charcoal:#2a2a2c;
  --slate:#66676b;
  --slate-line:#808185;
  --frame:#6d6e71;
  --footer:#3b3b3d;
  --paper:#ffffff;
  --icon:#8a8b8e;
  --icon-ring:#4f5054;
}
*{box-sizing:border-box;margin:0;padding:0}
html,body{width:784px;height:1200px;overflow:hidden;background:var(--paper)}
body{position:relative;font-family:"Open Sans",Arial,sans-serif;color:var(--ink)}

/* hero */
.hero{position:absolute;left:0;top:0;width:784px;height:576px;overflow:hidden;background:#b9b9b9}
.hero-visual{position:absolute;inset:0;
  background:
    radial-gradient(ellipse 150px 90px at 680px 150px,rgba(60,60,60,.75),rgba(60,60,60,0) 80%),
    radial-gradient(ellipse 220px 120px at 380px 250px,rgba(250,250,250,.7),rgba(250,250,250,0) 75%),
    radial-gradient(ellipse 160px 120px at 180px 120px,rgba(255,255,255,.8),rgba(255,255,255,0) 70%),
    radial-gradient(ellipse 130px 110px at 200px 310px,rgba(120,120,120,.55),rgba(120,120,120,0) 75%),
    radial-gradient(ellipse 200px 130px at 60px 470px,rgba(70,70,70,.7),rgba(70,70,70,0) 80%),
    radial-gradient(ellipse 260px 200px at 620px 330px,rgba(230,230,230,.8),rgba(230,230,230,0) 80%),
    linear-gradient(115deg,#7d7d7d 0%,#c8c8c8 30%,#e2e2e2 55%,#cfcfcf 75%,#9a9a9a 100%)}
.main-nav{position:absolute;left:346px;top:38px;width:86px;list-style:none;
  font-family:"Roboto Condensed",Arial,sans-serif;font-size:10px;color:#555}
.main-nav li{height:20px;line-height:20px;border-bottom:1px solid #a9a9a9;display:flex;justify-content:space-between}
.main-nav li:last-child{border-bottom:none}
.main-nav li.active{color:#fff;font-weight:700}
.brand{position:absolute;left:577px;top:33px;width:97px;height:33px;background:var(--green);
  color:#fff;font-family:"Raleway",Arial,sans-serif;font-weight:800;font-size:23px;
  line-height:33px;text-align:center;letter-spacing:1px}
.brand-social{position:absolute;left:589px;top:70px;display:flex;gap:5px}
.brand-social span{width:8px;height:8px;border-radius:50%;background:#5a5a5a}

.headline{position:absolute;left:112px;top:349px;font-family:"Raleway",Arial,sans-serif;
  font-weight:300;font-size:54px;line-height:1;letter-spacing:-1.2px}
.headline .line{display:block;position:absolute;left:0;white-space:nowrap;padding:4px 10px 0 13px}
.headline .l1{top:0;width:537px;height:62px;background:var(--charcoal);color:#fff}
.headline .l2{top:62px;width:471px;height:49px;background:var(--charcoal);color:#fff;padding-top:0}
.headline .l3{top:111px;height:59px;background:var(--green);color:var(--ink);padding:3px 12px 0 13px}
.headline .l3 b{font-weight:800;color:#fff;letter-spacing:-.5px}

/* sidebar */
.sidebar{position:absolute;left:0;top:576px;width:196px;height:546px;background:var(--slate);color:#fff}
.search{position:absolute;left:4px;top:14px;width:185px;height:28px;background:#fff;border:1px solid #ccc;
  font-size:9.5px;color:#999;line-height:26px;padding-left:22px}
.search svg{position:absolute;right:6px;top:6px}
.search::after{content:"";position:absolute;right:24px;top:6px;width:1px;height:15px;background:#ccc}
.sidebar h2{position:absolute;left:12px;top:58px;font-family:"Raleway",Arial,sans-serif;font-weight:300;
  font-size:21px;letter-spacing:-.5px}
.sidebar h2::after{content:"";position:absolute;left:0;top:32px;width:170px;height:1px;background:var(--slate-line)}
.news{position:absolute;left:11px;width:172px;font-size:6.6px;line-height:9.5px}
.news .num{position:absolute;left:0;top:0;width:24px;height:27px;background:var(--green);
  font-family:"Roboto Condensed",Arial,sans-serif;font-size:15px;line-height:27px;text-align:center}
.news .body{margin-left:33px}
.news time{display:block;font-size:7.2px;margin:-3px 0 1px}
.news a{color:var(--green);text-decoration:underline}
.news::after{content:"";position:absolute;left:0;top:50px;width:172px;height:1px;background:var(--slate-line)}
.news.last::after{display:none}
.read-more{position:absolute;left:43px;top:336px;width:54px;height:16px;background:#4e4f52;border:1px solid #7a7a7d;
  font-size:6.5px;line-height:14px;text-align:center;color:#bbb}
.social-grid{position:absolute;left:12px;top:382px;display:grid;grid-template-columns:repeat(6,24px);gap:9px 5px}
.social-grid span{position:relative;width:24px;height:24px;border-radius:50%;
  background:radial-gradient(circle at 40% 35%,#9a9b9e,#7b7c80);border:2px solid var(--icon-ring);
  box-shadow:inset 0 1px 2px rgba(0,0,0,.35)}
.social-grid span::after{content:"";position:absolute;left:6px;top:6px;width:8px;height:8px;border-radius:50%;
  border:2px solid var(--icon-ring)}

/* cards */
.card{position:absolute;width:180px;border:6px solid var(--frame);background:#fff;display:flex;flex-direction:column;padding:3px}
.card .photo{flex:1}
.card .caption{height:88px;background:var(--ink);color:#fff;padding:6px 8px}
.card.green .caption{background:var(--green)}
.caption header{display:flex;justify-content:space-between;align-items:center}
.caption h3{font-family:"Roboto Condensed",Arial,sans-serif;font-weight:700;font-size:14px}
.caption .dots{display:flex;gap:3px}
.caption .dots span{width:7px;height:7px;border-radius:50%;background:#bbb}
.card.green .dots span{background:#fff}
.caption p{font-size:6.6px;line-height:9px;margin:5px 0 4px;padding-bottom:4px;border-bottom:1px dotted #777}
.caption .meta{font-size:5.6px;line-height:12px;color:#ccc}
.caption .meta .row{display:flex;gap:14px;align-items:center}
.caption .meta i{display:inline-block;width:7px;height:6px;background:#ddd;border-radius:2px;margin-right:4px;vertical-align:middle}
.caption .meta .hl{color:var(--green)}
.card.green .meta .hl{color:#fff}

.to-top{position:absolute;left:721px;top:1092px;width:50px;height:30px;background:var(--footer);color:#fff;
  font-family:"Raleway",Arial,sans-serif;font-size:14px;text-align:center;padding-top:9px}
.to-top svg{position:absolute;left:18px;top:3px}

/* footer */
.site-footer{position:absolute;left:0;top:1122px;width:784px;height:78px;background:var(--footer);color:#ccc}
.footer-links{position:absolute;left:113px;top:24px;font-size:7.2px}
.copyright{position:absolute;left:113px;top:39px;font-size:6.5px;color:#888}
.contact{position:absolute;top:33px;font-size:10px;display:flex;align-items:center;gap:6px}
.contact.phone{left:362px}
.contact.mail{left:455px;gap:10px}
.footer-brand{position:absolute;left:584px;top:22px;font-family:"Raleway",Arial,sans-serif;font-weight:800;
  font-size:26px;color:#7a7a7c;letter-spacing:1px}
</style>
</head>
<body>

<section class="hero">
  <div class="hero-visual" role="img" aria-label="Greyscale photo of a hand reaching toward floating screens showing sky, a glass dome and solar panels"></div>
  <ul class="main-nav">
    <li class="active">HOME</li>
    <li>ABOUT US <span>+</span></li>
    <li>SOLUTIONS <span>+</span></li>
    <li>PARTNERS <span>+</span></li>
    <li>CONTACT US</li>
  </ul>
  <div class="brand">RALLY</div>
  <div class="brand-social"><span></span><span></span><span></span><span></span><span></span></div>
  <h1 class="headline">
    <span class="line l1">We believe we’re here</span>
    <span class="line l2">today because you</span>
    <span class="line l3">want to <b>RALLY.</b></span>
  </h1>
</section>

<aside class="sidebar">
  <div class="search">Enter Your Keywords Here...
    <svg width="13" height="13" viewBox="0 0 13 13"><circle cx="5" cy="5" r="4" fill="none" stroke="#333" stroke-width="1.8"/><line x1="8" y1="8" x2="12" y2="12" stroke="#333" stroke-width="2"/></svg>
  </div>
  <h2>LATEST NEWS</h2>
  <article class="news" style="top:102px"><div class="num">01</div><div class="body"><time>March 15, 2013</time><a>Lorem ipsum dolor sit amet</a>, consectetuer adipiscing elit, sed diam nonummy nibh euismod tincidunt ut laoreet dolore magna</div></article>
  <article class="news" style="top:160px"><div class="num">02</div><div class="body"><time>March 14, 2013</time><a>Lorem ipsum dolor sit amet</a>, consectetuer adipiscing elit, sed diam nonummy nibh euismod tincidunt ut laoreet dolore magna</div></article>
  <article class="news" style="top:221px"><div class="num">03</div><div class="body"><time>March 14, 2013</time><a>Lorem ipsum dolor sit amet</a>, consectetuer adipiscing elit, sed diam nonummy nibh euismod tincidunt ut laoreet dolore magna</div></article>
  <article class="news last" style="top:283px"><div class="num">03</div><div class="body"><time>March 13, 2013</time><a>Lorem ipsum dolor sit amet</a>, consectetuer adipiscing elit, sed diam nonummy nibh euismod tincidunt ut laoreet dolore magna</div></article>
  <div class="read-more">READ MORE</div>
  <div class="social-grid">
    <span></span><span></span><span></span><span></span><span></span><span></span>
    <span></span><span></span><span></span><span></span><span></span><span></span>
  </div>
</aside>

<article class="card" style="left:211px;top:590px;height:230px">
  <div class="photo" role="img" aria-label="Close-up of an energy-saving bulb among teal light bulbs" style="background:radial-gradient(ellipse at 40% 55%,#f3e7dc 0%,#cfd8d2 22%,rgba(79,143,140,0) 45%),linear-gradient(160deg,#4f8f8c,#2e5f60 70%,#6e9896)"></div>
  <div class="caption"><header><h3>Innovation</h3><div class="dots"><span></span><span></span><span></span><span></span><span></span></div></header>
    <p>Ut vel nulla lacus, non feugiat diam. Donec placerat nunc eu turpis scelerisque iaculis. Aenean...</p>
    <div class="meta"><div class="row"><span><i></i>5 Comments</span><span>March 12, 2013</span></div><div><i></i>25 People Like This..</div></div></div>
</article>

<article class="card" style="left:211px;top:830px;height:229px">
  <div class="photo" role="img" aria-label="Glowing world map with connected network icons" style="background:radial-gradient(circle at 65% 40%,#e07a2c,#3a5f8c 45%,#0f2338)"></div>
  <div class="caption"><header><h3>Solutions</h3><div class="dots"><span></span><span></span><span></span><span></span><span></span></div></header>
    <p>Ut vel nulla lacus, non feugiat diam. Donec placerat nunc eu turpis scelerisque iaculis. Aenean...</p>
    <div class="meta"><div class="row"><span><i></i>5 Comments</span><span>March 12, 2013</span></div><div><i></i>25 People Like This..</div></div></div>
</article>

<article class="card" style="left:401px;top:590px;height:242px">
  <div class="photo" role="img" aria-label="Sprinter crouched in the starting position" style="background:radial-gradient(ellipse at 45% 35%,#5a4034,rgba(46,36,31,0) 60%),linear-gradient(180deg,#7a7a7a,#2e241f 60%,#1a1a1a)"></div>
  <div class="caption"><header><h3>FOCUS</h3><div class="dots"><span></span><span></span><span></span><span></span><span></span></div></header>
    <p>Ut vel nulla lacus, non feugiat diam. Donec placerat nunc eu turpis scelerisque iaculis. Aenean...</p>
    <div class="meta"><div class="row hl"><span><i></i>5 Comments</span><span>March 12, 2013</span></div><div class="hl"><i></i>25 People Like This..</div></div></div>
</article>

<article class="card green" style="left:401px;top:843px;height:235px">
  <div class="photo" role="img" aria-label="Hand holding a smartphone" style="background:linear-gradient(150deg,#f4f4f4,#e3cdbf 55%,#d8d8d8)"></div>
  <div class="caption"><header><h3>Leadership</h3><div class="dots"><span></span><span></span><span></span><span></span></div></header>
    <p>Ut vel nulla lacus, non feugiat diam. Donec placerat nunc eu turpis scelerisque iaculis. Aenean...</p>
    <div class="meta"><div class="row hl"><span><i></i>5 Comments</span><span>March 12, 2013</span></div><div class="hl"><i></i>25 People Like This..</div></div></div>
</article>

<article class="card green" style="left:591px;top:590px;height:210px">
  <div class="photo" role="img" aria-label="Group of smiling colleagues" style="background:linear-gradient(120deg,#c9a58c,#7a4a34 50%,#3b2a22)"></div>
  <div class="caption"><header><h3>People</h3><div class="dots"><span></span><span></span><span></span><span></span><span></span></div></header>
    <p>Ut vel nulla lacus, non feugiat diam. Donec placerat nunc eu turpis scelerisque iaculis. Aenean...</p>
    <div class="meta"><div class="row hl"><span><i></i>5 Comments</span><span>March 12, 2013</span></div><div class="hl"><i></i>25 People Like This..</div></div></div>
</article>

<article class="card" style="left:591px;top:810px;height:238px">
  <div class="photo" role="img" aria-label="Portrait of a smiling businesswoman" style="background:linear-gradient(180deg,#ffffff,#e8d4c6 50%,#3a2a24)"></div>
  <div class="caption"><header><h3>Partners</h3><div class="dots"><span></span><span></span><span></span><span></span><span></span></div></header>
    <p>Ut vel nulla lacus, non feugiat diam. Donec placerat nunc eu turpis scelerisque iaculis. Aenean...</p>
    <div class="meta"><div class="row hl"><span><i></i>5 Comments</span><span>March 12, 2013</span></div><div class="hl"><i></i>25 People Like This..</div></div></div>
</article>

<div class="to-top"><svg width="14" height="7" viewBox="0 0 14 7"><polyline points="1,6 7,1 13,6" fill="none" stroke="#fff" stroke-width="1.5"/></svg>TOP</div>

<footer class="site-footer">
  <nav class="footer-links">HOME . ABOUT US . SOLUTIONS . PARTNERS . CONTACT US</nav>
  <div class="copyright">© 2013 RALLY. All rights reserved.</div>
  <div class="contact phone"><svg width="12" height="12" viewBox="0 0 12 12"><path d="M2 1 L4.5 1 L5.5 3.8 L4 5 Q5 7.2 7 8 L8.2 6.5 L11 7.5 L11 10 Q10 11 8.5 11 Q2 10 1 3.5 Q1 2 2 1Z" fill="#8cc43f"/></svg>123.555.0148</div>
  <div class="contact mail"><svg width="16" height="11" viewBox="0 0 16 11"><rect x="0.5" y="0.5" width="15" height="10" fill="#8cc43f"/><polyline points="0.5,0.5 8,6 15.5,0.5" fill="none" stroke="#3b3b3d" stroke-width="1.2"/></svg>info@rallyco.com</div>
  <div class="footer-brand">RALLY</div>
</footer>

</body>
</html>
```